Bref créative
Skyward Valuers - Promotional Handouts
Tri-Fold Brochure and Postcard for direct mail
Two items needed:
1. - Tri-fold Brochure (Letter Size) used for distribution face to face.
2. - Postcard (Standard Size) used for direct mail campaigns.
Use the content in the attached files.
Or feel free to add/delete/change any of the copy, or create your own copy (make sure to spell/grammar check). Keep it within the feel of the company.
This company appraises aircraft (Airplanes, Helicopters, Jets, etc;)
My current website is ( www.skywardval-example.com ) this will give you a sense of what kind of business it is. (Still haven't updated the site with the new logo)
Aviation
These will go out to potential customers/clients who would like to have their aircraft appraised. Usually the people who own aircraft or who need an aircraft appraised are corporate professionals.
I deal with a lot of 'Type A' personalities, people who own aircraft tend to be in the higher income bracket and also have high standards. They will use my company to perform research for aircraft sales and acquisition.
They will use my company as a tool to help them buy/sell an aircraft or to have it appraised for insurance purposes.
I need to present a very high class elegant, professional looking design.
Clean, simple, and elegant.
This is the logo to be used.
The look and feel from the stationary pack to give you a sense of the type of designs I'm looking for.
My Mission statement (Copy to be used if desired)
Airports that I will travel to with no extra fee (Copy to be used if desired)
My contact information (Copy to be used if desired)
The steps to the appraisal process (Copy to be used if desired)
Information regarding the logo (colors, fonts, etc..)

```html
<!DOCTYPE html>
<html lang="en">
<head>
<meta charset="utf-8">
<title>Skyward Valuers – Brochure Inside</title>
<link href="https://fonts.googleapis.com/css2?family=Questrial&family=EB+Garamond:ital,wght@0,400;1,400&display=swap" rel="stylesheet">
<style>
  :root {
    --brand-red: #c8102e;
    --brand-red-dark: #7a0a1a;
    --ink: #3a3a3a;
    --heading: #4a4a4a;
    --quote-bg: #c9dcee;
    --quote-ink: #6a6f75;
    --paper: #ffffff;
  }
  * { margin: 0; padding: 0; box-sizing: border-box; }
  html, body { width: 1200px; height: 927px; overflow: hidden; background: var(--paper); }
  .brochure-inside { position: relative; width: 1200px; height: 927px; background: var(--paper); }
  .top-band {
    position: absolute; left: 0; top: 0; width: 1200px; height: 22px;
    background: linear-gradient(90deg, var(--brand-red-dark) 0%, var(--brand-red) 45%, var(--brand-red-dark) 100%);
  }
  .panel { position: absolute; top: 98px; }
  .panel h2 {
    font-family: "Questrial", sans-serif; font-weight: 400;
    font-size: 27px; color: var(--heading); margin-bottom: 20px; letter-spacing: 0.2px;
  }
  .body-copy { font-family: "EB Garamond", serif; font-size: 15px; line-height: 1.3; color: var(--ink); }

  .panel-process { left: 50px; width: 300px; }
  .process-intro { width: 240px; margin-bottom: 16px; }
  .step-list { list-style: none; }
  .step-list li { display: flex; margin-bottom: 14px; }
  .step-label { flex: 0 0 48px; }
  .step-text { width: 190px; }

  .panel-airports { left: 408px; width: 330px; }
  .airport-list { list-style: none; margin-left: 66px; width: 240px; }
  .airport-list li { position: relative; padding-left: 12px; margin-bottom: 19px; }
  .airport-list li::before { content: "•"; position: absolute; left: 0; }
  .airport-note { font-style: italic; font-size: 14px; margin-left: 66px; margin-top: -6px; }

  .panel-contact { left: 822px; width: 340px; }
  .contact-block { font-style: normal; }

  .mission-quote {
    position: absolute; left: 822px; top: 330px; width: 342px; height: 496px;
    background: var(--quote-bg); border-radius: 42px 0 0 0;
    padding: 26px 40px 0 52px;
    font-family: "Questrial", sans-serif; font-size: 21px; line-height: 27px; color: var(--quote-ink);
  }
  .mission-quote p { margin-bottom: 27px; padding-left: 20px; width: 250px; }
  .quote-mark { font-size: 46px; line-height: 0; color: var(--quote-ink); vertical-align: -16px; }
  .quote-open { margin-left: -26px; margin-right: 4px; }
  .highlight { color: var(--brand-red); }
  .mission-quote .quote-author { text-align: right; font-style: italic; width: 250px; }
</style>
</head>
<body>
<main class="brochure-inside">
  <div class="top-band"></div>

  <section class="panel panel-process">
    <h2>Appraisal Process:</h2>
    <p class="body-copy process-intro">Generally the appraisal process takes only one week from first contact until the appraisal report has been completed. Here is how a typical appraisal process works:</p>
    <ol class="step-list body-copy">
      <li><span class="step-label">Step 1:</span><span class="step-text">Make contact<br>(email, online form, phone)</span></li>
      <li><span class="step-label">Step 2:</span><span class="step-text">Schedule aircraft viewing time and place, answer questions, discuss aircraft history, appraisal fee.</span></li>
      <li><span class="step-label">Step 3:</span><span class="step-text">Appraise the aircraft, logbooks and supporting documents.</span></li>
      <li><span class="step-label">Step 4:</span><span class="step-text">Research and compile the aircraft's history and create the Appraisal Report.</span></li>
      <li><span class="step-label">Step 5:</span><span class="step-text">Appraisal completed,<br>submit payment</span></li>
      <li><span class="step-label">Step 6:</span><span class="step-text">Payment received<br>Certificated Appraisal Report sent via courier/express/post.</span></li>
      <li><span class="step-label">Step 7:</span><span class="step-text">Follow up phone call, answer any questions you have regarding the report.</span></li>
    </ol>
  </section>

  <section class="panel panel-airports">
    <h2>Home Airports: *</h2>
    <ul class="airport-list body-copy">
      <li>KRL - Redfern Park Airport</li>
      <li>X41 - Halden Airport</li>
      <li>NRB - Northern Ridge Regional Airport/ Calloway Field</li>
      <li>BWK - Brookwick Municipal Airport</li>
      <li>X07 - Parkway Airport</li>
      <li>ELR - Elmsford Regional Airport</li>
      <li>QLT - Larkton Executive Airport</li>
      <li>MVR - Millvale Regional Airport</li>
      <li>3X8 - Bayside Airport</li>
      <li>GVC - Greyston County Airpark</li>
      <li>RVX - Riverbend Airfield</li>
      <li>X22 - Hillcrest Airport</li>
      <li>TPX - Thornton Airport</li>
      <li>HWK Westbrook-Fairmont Airport</li>
      <li>X35 Kingsport Executive Airport/Hale Field</li>
      <li>OKR Oakridge Regional Airport</li>
    </ul>
    <p class="body-copy airport-note">* Other Airports may increase the cost.<br>&nbsp;&nbsp;Call for quotes!</p>
  </section>

  <section class="panel panel-contact">
    <h2>Contact Information:</h2>
    <address class="body-copy contact-block">
      Skyward Valuers<br>
      Evan Marsh<br>
      4820 Harbor View Lane #210<br>
      Ashford, VA 20100<br>
      Evan @ (555) 014-2290(Evan)<br>
      Email: Evan@SkywardVal.com
    </address>
  </section>

  <aside class="mission-quote">
    <p><span class="quote-mark quote-open">&ldquo;</span>I strive to work with a spirit of honesty, integrity and accountability and I will treat each customer with respect, dignity, and confidentiality.</p>
    <p>I will provide my customers with <span class="highlight">outstanding service</span> by creating reports of the highest caliber. <span class="quote-mark">&rdquo;</span></p>
    <p class="quote-author">- Evan Marsh</p>
  </aside>
</main>
</body>
</html>
```